Letter Head and Business cards
Medical company
Project: Letter Head and Business cards
Letter Head and Business cards  - Medical
Creative Brief
Professional
Colin Marsh
Manager
4815 Alder Bend Road Fernvale, IN 46188
tlarkinmedico@quillpost.example
Business logo or something creative

```html
<!DOCTYPE html>
<html lang="en">
<head>
<meta charset="utf-8">
<title>T Larkin Medico – Stationery</title>
<link rel="stylesheet" href="https://fonts.googleapis.com/css2?family=Lato:wght@400;700&display=swap">
<style>
  :root {
    --backdrop: #e9e4dc;
    --paper: #ffffff;
    --brand-blue: #1e7fd8;
    --brand-blue-light: #4aa3ec;
    --brand-navy: #133a6a;
    --ink: #3b4350;
    --ink-soft: #7a8290;
    --shadow: 0 6px 18px rgba(40, 30, 20, 0.22);
  }
  * { box-sizing: border-box; margin: 0; padding: 0; }
  html, body { width: 1200px; height: 799px; overflow: hidden; }
  body {
    background: var(--backdrop);
    font-family: "Lato", Arial, sans-serif;
    color: var(--ink);
    position: relative;
  }
  .sheet { position: absolute; background: var(--paper); box-shadow: var(--shadow); overflow: hidden; }

  .wordmark { display: flex; align-items: center; gap: 8px; }
  .wordmark-dot { width: 14px; height: 14px; border-radius: 50%; background: var(--brand-blue); }
  .wordmark-name { font-weight: 700; color: var(--brand-blue); font-size: 20px; letter-spacing: 0.5px; }

  .contact { font-size: 8px; line-height: 1.45; color: var(--ink-soft); }

  .corner-block {
    position: absolute; left: 0; bottom: 0;
    background: linear-gradient(135deg, var(--brand-blue-light), var(--brand-blue));
  }

  /* Letterhead */
  .letterhead { left: 340px; top: 30px; width: 440px; height: 600px; }
  .letterhead .wordmark { position: absolute; left: 34px; top: 40px; }
  .letterhead .contact { position: absolute; right: 34px; top: 34px; text-align: left; }
  .letterhead .corner-block { width: 120px; height: 150px; }

  /* Envelope */
  .envelope { left: 40px; top: 470px; width: 520px; height: 250px; }
  .envelope .wordmark { position: absolute; left: 26px; top: 28px; }
  .envelope .wordmark-name { font-size: 17px; }
  .envelope .contact { position: absolute; left: 26px; top: 62px; }
  .envelope .corner-block { width: 70px; height: 110px; }

  /* Business cards */
  .card { width: 320px; height: 180px; }
  .card-back {
    left: 840px; top: 110px;
    background: var(--brand-navy);
    display: flex; align-items: center; justify-content: center;
  }
  .card-back .wordmark-dot { background: var(--paper); }
  .card-back .wordmark-name { color: var(--paper); font-size: 22px; }

  .card-front { left: 840px; top: 330px; }
  .card-front .corner-block { width: 90px; height: 180px; }
  .card-front .holder { position: absolute; left: 150px; top: 26px; }
  .holder-name { font-weight: 700; font-size: 12px; color: var(--brand-blue); }
  .holder-role { font-size: 9px; color: var(--ink-soft); margin-bottom: 10px; }
  .card-front .contact { position: absolute; left: 150px; top: 90px; }
</style>
</head>
<body>

  <section class="sheet letterhead" aria-label="Letterhead">
    <div class="wordmark">
      <span class="wordmark-dot"></span>
      <span class="wordmark-name">T Larkin Medico</span>
    </div>
    <div class="contact">
      4815 Alder Bend Road<br>
      Fernvale, IN 46188<br>
      P: (317) 555-0142<br>
      tlarkinmedico@quillpost.example
    </div>
    <div class="corner-block" role="img" aria-label="Blue brand corner decoration"></div>
  </section>

  <section class="sheet envelope" aria-label="Envelope">
    <div class="wordmark">
      <span class="wordmark-dot"></span>
      <span class="wordmark-name">T Larkin Medico</span>
    </div>
    <div class="contact">
      4815 Alder Bend Road<br>
      Fernvale, IN 46188
    </div>
    <div class="corner-block" role="img" aria-label="Blue brand corner decoration"></div>
  </section>

  <section class="sheet card card-back" aria-label="Business card back">
    <div class="wordmark">
      <span class="wordmark-dot"></span>
      <span class="wordmark-name">T Larkin Medico</span>
    </div>
  </section>

  <section class="sheet card card-front" aria-label="Business card front">
    <div class="corner-block" role="img" aria-label="Blue brand side decoration"></div>
    <div class="holder">
      <div class="holder-name">Colin Marsh</div>
      <div class="holder-role">Manager</div>
    </div>
    <div class="contact">
      4815 Alder Bend Road<br>
      Fernvale, IN 46188<br>
      P: (317) 555-0142<br>
      tlarkinmedico@quillpost.example
    </div>
  </section>

</body>
</html>
```